Business Card Design Project

Recently had a new logo made up for my company and new business cards done as well. I have attached the logos for your viewing. Additional projects may be needed. Good luck!

Industry/Entity Type

Business

```html
<!DOCTYPE html>
<html lang="en">
<head>
<meta charset="utf-8">
<title>Harrow Financial Group – Business Card</title>
<link rel="stylesheet" href="https://fonts.googleapis.com/css2?family=Lato:wght@400&display=swap">
<style>
  :root {
    --page: #ffffff;
    --frame: #9a9a9a;
    --card-dark: #25242c;
    --card-red: #ec1c24;
    --gold: #c9b27c;
    --white: #ffffff;
    --icon-ink: #25242c;
  }
  * { margin: 0; padding: 0; box-sizing: border-box; }
  html, body {
    width: 1200px; height: 900px; overflow: hidden;
    background: var(--page);
    font-family: "Lato", Arial, sans-serif;
  }
  .canvas {
    position: relative; width: 1200px; height: 900px;
    border-right: 1px solid var(--frame);
    border-bottom: 1px solid var(--frame);
  }
  .card { position: absolute; left: 232px; width: 736px; height: 422px; }
  .card--front { top: 16px; background: var(--card-dark); }
  .card--back { top: 455px; background: var(--card-red); }

  .brand {
    position: absolute; display: flex; align-items: center; gap: 10px;
    color: var(--gold); font-weight: 400; line-height: 1.15;
  }
  .brand__square { flex: none; width: 14px; height: 14px; background: var(--gold); }
  .brand__name { font-size: 24px; }
  .card--front .brand { left: 42px; top: 100px; width: 190px; }

  .brand-panel {
    position: absolute; left: 285px; top: 76px; width: 166px; height: 206px;
    background: var(--card-dark);
    display: flex; align-items: center; justify-content: center;
  }
  .brand-panel .brand { position: static; width: 130px; }

  .holder { position: absolute; left: 328px; top: 156px; color: var(--gold); }
  .holder__name { font-size: 31px; line-height: 1.1; }
  .holder__title { font-size: 18px; margin-top: 4px; }

  .contacts { position: absolute; left: 326px; top: 271px; list-style: none; }
  .contacts li {
    display: flex; align-items: center; gap: 9px;
    color: var(--white); font-size: 21px; height: 29.5px;
  }
  .contacts svg { width: 25px; height: 25px; flex: none; }

  .address {
    position: absolute; left: 0; right: 0; top: 364px;
    text-align: center; color: var(--white); font-size: 18.5px;
  }
</style>
</head>
<body>
<div class="canvas">
  <section class="card card--front">
    <div class="brand">
      <span class="brand__square"></span>
      <span class="brand__name">Harrow Financial Group</span>
    </div>
    <div class="holder">
      <p class="holder__name">Daniel R. Harrow</p>
      <p class="holder__title">Estate Planning and Insurance Specialist</p>
    </div>
    <ul class="contacts">
      <li>
        <svg viewBox="0 0 24 24" aria-hidden="true"><circle cx="12" cy="12" r="12" fill="var(--gold)"/><rect x="5.5" y="7.5" width="13" height="9" fill="none" stroke="var(--icon-ink)" stroke-width="1.5"/><path d="M5.5 7.5 12 13l6.5-5.5M5.5 16.5l4.5-4.5M18.5 16.5 14 12" fill="none" stroke="var(--icon-ink)" stroke-width="1.3"/></svg>
        Dharrow@harrowfinancial.com
      </li>
      <li>
        <svg viewBox="0 0 24 24" aria-hidden="true"><circle cx="12" cy="12" r="12" fill="var(--gold)"/><path d="M8.2 5.5c.6-.4 1.2-.2 1.5.3l1.4 2.4c.3.5.2 1.1-.3 1.4l-.9.6c.6 1.6 1.9 3 3.6 3.8l.6-.9c.3-.5.9-.6 1.4-.3l2.4 1.4c.5.3.7.9.3 1.5l-.8 1.2c-.5.7-1.4 1-2.2.7C10 16.3 7.2 13.4 6 9.3c-.2-.8.1-1.7.8-2.2z" fill="var(--icon-ink)"/></svg>
        516-555-0142
      </li>
      <li>
        <svg viewBox="0 0 24 24" aria-hidden="true"><circle cx="12" cy="12" r="12" fill="var(--gold)"/><rect x="8" y="5" width="8" height="5" fill="none" stroke="var(--icon-ink)" stroke-width="1.3"/><rect x="5.5" y="10" width="13" height="6" fill="var(--icon-ink)"/><rect x="8" y="14" width="8" height="5" fill="var(--gold)" stroke="var(--icon-ink)" stroke-width="1.3"/></svg>
        516-555-0187
      </li>
      <li>
        <svg viewBox="0 0 24 24" aria-hidden="true"><circle cx="12" cy="12" r="12" fill="var(--gold)"/><g fill="none" stroke="var(--icon-ink)" stroke-width="1.2"><circle cx="12" cy="12" r="6.5"/><ellipse cx="12" cy="12" rx="2.8" ry="6.5"/><path d="M5.5 12h13M6.5 8.7h11M6.5 15.3h11"/></g></svg>
        www.harrowfinancial.com
      </li>
    </ul>
  </section>

  <section class="card card--back">
    <div class="brand-panel">
      <div class="brand">
        <span class="brand__square"></span>
        <span class="brand__name">Harrow Financial Group</span>
      </div>
    </div>
    <p class="address">4200 Meadow Turnpike, Suite 310E, Brookvale, New York 11700</p>
  </section>
</div>
</body>
</html>
```